Commercial Broker Profile Flyer

I need a one-page flyer created that will serve as a profile report for individual brokers within a commercial real estate firm. The flyer will include company branding, agent photo, bio, and other information. I would like to have the source file available for future editing preferably in a Publisher file format. A copy of a company brochure is included and would like to have this profile flyer similar to keep company branding consistent. Our company website is www.holbrookvalere.com for any other questions on branding.
Updates

Target Market(s)

Professional

Industry/Entity Type

Real Estate Agent

Requirements
Must have
• One page
• Source files MUST include a .PUB file that I can update in the future
• All of the information in the uploaded "content" file
• Company branding
• Must be 8.5"x11"
Should not have
• Do not use stock photos or property photos from the attachments. I only want the broker photo and company logo.

```html
<!DOCTYPE html>
<html lang="en">
<head>
<meta charset="utf-8">
<title>Broker Profile – Holbrook - Valere Real Estate</title>
<link rel="stylesheet" href="https://fonts.googleapis.com/css2?family=Cormorant+Garamond:wght@500&family=PT+Sans:wght@400;700&display=swap">
<style>
  :root {
    --brand-green: #1c6a3b;
    --brand-green-dark: #0f5a2c;
    --page-bg: #dedede;
    --paper: #f7f7f7;
    --paper-shade: #ececec;
    --ink: #1d1d1d;
    --white: #ffffff;
    --mark-tint: rgba(28,106,59,0.07);
  }
  * { margin: 0; padding: 0; box-sizing: border-box; }
  html, body { width: 1200px; height: 618px; overflow: hidden; }
  body { background: var(--page-bg); position: relative; font-family: "PT Sans", Arial, sans-serif; color: var(--ink); }

  .flyer {
    position: absolute; left: 388px; top: 9px; width: 424px; height: 600px;
    background: linear-gradient(160deg, var(--paper) 0%, var(--paper-shade) 100%);
    box-shadow: 0 2px 8px rgba(0,0,0,0.25);
    overflow: hidden;
  }
  .header-band { position: absolute; left: 0; top: 0; width: 424px; height: 185px; }

  .brand-mark {
    position: absolute; left: 22px; top: 29px; width: 70px; height: 70px;
    border-radius: 50%; border: 2px solid var(--white);
  }
  .brand-name {
    position: absolute; left: 98px; top: 26px;
    font-family: "Cormorant Garamond", Georgia, serif; font-weight: 500;
    font-size: 34px; line-height: 1; color: var(--white); white-space: nowrap;
  }
  .brand-sub {
    position: absolute; left: 116px; width: 270px; text-align: center;
    font-family: "Cormorant Garamond", Georgia, serif; font-weight: 500;
    color: var(--white); text-transform: uppercase; white-space: nowrap;
  }
  .brand-sub--entity { top: 68px; font-size: 15px; letter-spacing: 3.4px; }
  .brand-rule { position: absolute; left: 116px; top: 89px; width: 270px; height: 1px; background: var(--white); }
  .brand-sub--tagline { top: 99px; font-size: 11.5px; letter-spacing: 2.6px; }

  .agent-name {
    position: absolute; right: 174px; top: 178px; text-align: right;
    color: var(--brand-green); font-weight: 700; font-size: 11.5px; white-space: nowrap;
  }
  .agent-title {
    position: absolute; right: 174px; top: 192px; text-align: right;
    font-weight: 700; font-size: 8.4px; white-space: nowrap;
  }
  .agent-photo {
    position: absolute; left: 266px; top: 160px; width: 84px; height: 116px;
    border-radius: 50%;
    background: radial-gradient(ellipse at 50% 40%, #c9b9a8 0%, #8d8a86 55%, #5c5f63 100%);
    box-shadow: 0 0 0 2px rgba(255,255,255,0.8);
  }
  .contact-list {
    position: absolute; right: 166px; top: 218px; list-style: none; text-align: right;
    font-size: 7.6px; line-height: 13px; white-space: nowrap;
  }
  .contact-list .label { color: var(--brand-green); }

  .section-rule { position: absolute; left: 0; height: 2px; background: var(--brand-green); }
  .section-title {
    position: absolute; color: var(--brand-green); font-weight: 700; font-size: 12px; line-height: 1;
  }
  .bio {
    position: absolute; left: 47px; top: 295px; width: 362px;
    font-size: 7.45px; line-height: 10.6px; text-align: justify;
  }
  .bio p + p { margin-top: 3px; }
  .plain-list {
    position: absolute; left: 118px; list-style: none; font-size: 7.6px; line-height: 10.3px;
  }
  .mark-tint {
    position: absolute; left: 282px; top: 412px; width: 128px; height: 128px;
    border-radius: 50%; background: var(--mark-tint);
  }
</style>
</head>
<body>
  <article class="flyer">
    <svg class="header-band" viewBox="0 0 424 185" aria-hidden="true">
      <defs>
        <linearGradient id="bandFill" x1="0" y1="0" x2="0" y2="1">
          <stop offset="0" stop-color="#1c6a3b"/>
          <stop offset="1" stop-color="#0f5a2c"/>
        </linearGradient>
      </defs>
      <path d="M0 0 H424 V138 C330 142 240 150 170 162 C110 172 50 168 0 158 Z" fill="url(#bandFill)"/>
      <path d="M0 158 C50 168 110 172 170 162 C240 150 330 142 424 138" fill="none" stroke="#ffffff" stroke-width="1.2" opacity="0.7"/>
    </svg>

    <div class="brand-mark" aria-hidden="true"></div>
    <div class="brand-name">Holbrook - Valere</div>
    <div class="brand-sub brand-sub--entity">Real Estate, LLC</div>
    <div class="brand-rule"></div>
    <div class="brand-sub brand-sub--tagline">Commercial • Investment</div>

    <div class="mark-tint" aria-hidden="true"></div>

    <h1 class="agent-name">T. Russell Halden, CCPA, CRL</h1>
    <p class="agent-title">Principal / Broker in Charge</p>
    <div class="agent-photo" role="img" aria-label="Portrait photo of the broker"></div>
    <ul class="contact-list">
      <li><span class="label">Office Phone:</span> (555) 214-3390 ext. 202</li>
      <li><span class="label">Cell Phone:</span> &nbsp;(555) 370-6612</li>
      <li><span class="label">Email:</span> russell@holbrookvalere.com</li>
      <li><span class="label">Website:</span> www.holbrookvalere.com</li>
    </ul>

    <div class="section-rule" style="top:281px; width:44px;"></div>
    <h2 class="section-title" style="left:48px; top:276px;">Bio</h2>
    <div class="bio">
      <p>Russell began his real estate career in 2005 and has completed $75+ million in transactions representing sellers and buyers of commercial real estate, providing tenant representation, and leasing of retail and office properties. Prior to beginning his real estate career, Russell served over five years in the Army Reserves and attended Eastbrook State University.</p>
      <p>Russell has earned the prestigious Certified Commercial Property Advisor (CCPA) designation as well as the Certified Retail Lessor (CRL) designation. Russell is a member of the Retail Property Leasing Council (RPLC), the Carolina Plains Realtor Association, the Riverford County Chamber of Commerce, and serves on the board of directors for the State CCPA Chapter, the Sandridge Community Center, and the Pinecrest Realtors Association. Russell is a licensed real estate broker in two states.</p>
    </div>

    <div class="section-rule" style="top:408px; width:114px;"></div>
    <h2 class="section-title" style="left:118px; top:403px;">Clients Served</h2>
    <ul class="plain-list" style="top:418px;">
      <li>Crestline Biscuits</li>
      <li>Ninefold Burgers</li>
      <li>Clipline Salons</li>
      <li>Roadway Tire Depot</li>
      <li>Sweetcrumb Bakery</li>
      <li>Meridian Home Care</li>
      <li>Kinfolk Services</li>
      <li>Harbor Edge</li>
      <li>Bluewater Bottling Co.</li>
    </ul>

    <div class="section-rule" style="top:525px; width:114px;"></div>
    <h2 class="section-title" style="left:118px; top:520px;">Professional Affiliations</h2>
    <ul class="plain-list" style="top:535px;">
      <li>Certified Commercial Property Advisor (designee)</li>
      <li>Retail Property Leasing Council</li>
      <li>Pinecrest Realtors Association</li>
      <li>State Realtors Commercial Forms Committee</li>
    </ul>
  </article>
</body>
</html>
```